Postcard Design

we need a post card design for our company in worth, illinois called Velmora Dental lab we would like to see designs that use the colors blue and gray. We are a dental lab specializing in removable dentures and partials. These particular post cards are emphasizing doing relines and repairs the same day our address is 48207 N Cobbet ave Brenhaven NV. Phone 708-555-0194

Industry/Entity Type

Dental

```html
<!DOCTYPE html>
<html lang="en">
<head>
<meta charset="utf-8">
<title>Velmora Dental lab – Postcard</title>
<link href="https://fonts.googleapis.com/css2?family=Fredoka:wght@500;600;700&family=Hind:wght@400;500;600;700&display=swap" rel="stylesheet">
<style>
  :root{
    --page:#a7a8ab;
    --white:#ffffff;
    --navy:#2b3990;
    --blue:#1f6fc4;
    --sky:#2a9be0;
    --ink:#1a1a1a;
    --grey:#6d6e71;
    --grey-light:#d1d3d4;
    --slot:#e6e7e8;
  }
  *{margin:0;padding:0;box-sizing:border-box}
  html,body{width:1200px;height:483px;overflow:hidden;background:var(--page)}
  body{position:relative;font-family:"Hind",sans-serif}
  .card{position:absolute;overflow:hidden;background:var(--white)}
  .front{left:30px;top:26px;width:557px;height:429px;
    background:linear-gradient(180deg,#e4ecf4 0%,#f3f6f9 40%,#ffffff 60%)}
  .back{left:617px;top:24px;width:558px;height:430px}
  .abs{position:absolute}

  /* front */
  .couple-photo{left:0;top:0;width:268px;height:372px;
    background:linear-gradient(160deg,#c9a184 0%,#b98c72 40%,#7d7f86 75%,#d8b4aa 100%)}
  .front-waves{left:0;top:0;width:557px;height:429px}
  .brand{left:229px;top:30px;font-family:"Fredoka",sans-serif;font-weight:600;font-size:31px;line-height:1.1;color:var(--navy);white-space:nowrap}
  .make-you{left:346px;top:82px;font-family:"Fredoka",sans-serif;font-weight:500;font-size:15px;line-height:1;color:var(--grey)}
  .smile{left:294px;top:88px;font-family:"Fredoka",sans-serif;font-weight:700;font-size:78px;line-height:1;color:var(--blue);letter-spacing:-1px}
  .front-ribbon{left:246px;top:158px;width:311px;height:58px}
  .front-ribbon-text{left:289px;top:173px;font-family:"Fredoka",sans-serif;font-weight:500;font-size:22px;line-height:1.1;color:var(--white)}
  .specialty{left:290px;top:236px;font-weight:600;font-size:15px;line-height:19px;color:var(--ink);white-space:nowrap}
  .experience{left:290px;top:281px;font-size:15px;line-height:17px;color:var(--navy);width:132px}
  .experience strong{font-weight:700}
  .front-hex{left:433px;top:283px;width:118px;height:103px}
  .call-label{left:26px;top:384px;font-size:12.5px;line-height:14px;color:var(--white)}
  .call-phone{left:26px;top:398px;font-weight:700;font-size:20px;line-height:22px;color:var(--white);letter-spacing:.3px}
  .front-address{right:19px;top:389px;text-align:right;font-size:12.5px;line-height:17px;color:var(--white);white-space:nowrap}

  /* back */
  .back-swoosh{left:0;top:0;width:558px;height:430px}
  .top-band{left:22px;top:0;width:311px;height:26px;background:linear-gradient(90deg,var(--navy),var(--sky));
    color:var(--white);font-size:10.5px;line-height:27px;padding-left:22px;white-space:nowrap}
  .lab-photo{left:22px;top:26px;width:311px;height:159px;
    background:linear-gradient(90deg,#c7b9a4 0%,#8a5a3a 30%,#d9d6d1 60%,#bfc3c7 100%)}
  .back-ribbon{left:0;top:95px;width:300px;height:52px}
  .back-ribbon-text{left:24px;top:104px;font-family:"Fredoka",sans-serif;font-weight:500;font-size:16px;line-height:15px;color:var(--white);white-space:nowrap}
  .story{left:62px;top:200px;font-size:11px;line-height:14px;color:#333;white-space:nowrap}
  .back-hex{left:4px;top:273px;width:90px;height:80px}
  .same-day{left:104px;top:271px;width:200px;font-weight:600;font-size:11px;line-height:13px;color:var(--blue)}
  .call-today{left:104px;top:298px;font-weight:600;font-size:14px;line-height:16px;color:var(--blue);white-space:nowrap}
  .back-phone{left:104px;top:320px;font-weight:700;font-size:30px;line-height:34px;color:var(--navy);letter-spacing:.5px;white-space:nowrap}
  .back-address{left:104px;top:354px;font-size:15.5px;line-height:18px;color:var(--blue);white-space:nowrap}
  .stamp-slot{left:463px;top:20px;width:73px;height:71px;background:var(--slot)}
  .address-slot{left:353px;top:131px;width:183px;height:124px;background:var(--slot)}
</style>
</head>
<body>

<section class="card front">
  <div class="abs couple-photo" role="img" aria-label="Smiling couple hugging, with a pair of full dentures in the foreground"></div>

  <svg class="abs front-waves" viewBox="0 0 557 429" aria-hidden="true">
    <defs>
      <linearGradient id="frontBand" x1="0" y1="0" x2="1" y2="0">
        <stop offset="0" stop-color="#2b3990"/><stop offset=".5" stop-color="#1f6fc4"/><stop offset="1" stop-color="#2a9be0"/>
      </linearGradient>
    </defs>
    <path d="M0 348 C160 350 360 372 557 355 L557 429 L0 429 Z" fill="#d1d3d4"/>
    <path d="M0 358 C170 362 360 392 557 370 L557 429 L0 429 Z" fill="url(#frontBand)"/>
  </svg>

  <div class="abs brand">Velmora Dental lab</div>
  <div class="abs smile">Smile</div>
  <div class="abs make-you">Make you</div>

  <svg class="abs front-ribbon" viewBox="0 0 311 58" aria-hidden="true">
    <polygon points="0,0 32,6 32,48 12,52 22,28" fill="#1c2570"/>
    <polygon points="22,6 311,6 311,48 22,48" fill="#2b3990"/>
    <line x1="26" y1="10" x2="311" y2="10" stroke="#ffffff" stroke-opacity=".5" stroke-dasharray="3 2"/>
    <line x1="26" y1="44" x2="311" y2="44" stroke="#ffffff" stroke-opacity=".5" stroke-dasharray="3 2"/>
    <polygon points="22,48 311,48 311,56 30,56" fill="#4a4b4d"/>
  </svg>
  <div class="abs front-ribbon-text">Relines And Repairs</div>

  <p class="abs specialty">Dental Lab Specializing In<br>Removable Dentures And Partials.</p>
  <p class="abs experience"><strong>We have over 35 years experience.</strong> We can do relines and repairs the same day</p>

  <svg class="abs front-hex" viewBox="0 0 120 105" role="img" aria-label="Technician polishing a partial denture">
    <defs>
      <linearGradient id="hexFront" x1="0" y1="0" x2="1" y2="1">
        <stop offset="0" stop-color="#d8c7a6"/><stop offset=".5" stop-color="#e9a6ad"/><stop offset="1" stop-color="#f1f2f2"/>
      </linearGradient>
    </defs>
    <polygon points="30,2 90,2 118,52 90,103 30,103 2,52" fill="url(#hexFront)" stroke="#bcbec0" stroke-width="4"/>
  </svg>

  <div class="abs call-label">Can you call me?</div>
  <div class="abs call-phone">708-555-0194</div>
  <p class="abs front-address">Velmora dental lab.<br>48207 N Cobbet ave. Brenhaven, NV. 89931</p>
</section>

<section class="card back">
  <svg class="abs back-swoosh" viewBox="0 0 558 430" aria-hidden="true">
    <defs>
      <linearGradient id="backBand" x1="0" y1="0" x2="0" y2="1">
        <stop offset="0" stop-color="#2b3990"/><stop offset=".6" stop-color="#1f6fc4"/><stop offset="1" stop-color="#2a9be0"/>
      </linearGradient>
    </defs>
    <path d="M26 0 L40 0 C50 150 78 320 118 430 L86 430 C52 300 32 150 26 0 Z" fill="#d1d3d4"/>
    <path d="M0 0 L26 0 C32 150 52 300 86 430 L0 430 Z" fill="url(#backBand)"/>
  </svg>

  <div class="abs top-band">Velmora dental lab. 48207 N Cobbet ave. Brenhaven, NV. 89931</div>
  <div class="abs lab-photo" role="img" aria-label="Interior of the dental lab with wooden doors and equipment"></div>

  <svg class="abs back-ribbon" viewBox="0 0 300 52" aria-hidden="true">
    <defs>
      <linearGradient id="greyRibbon" x1="0" y1="0" x2="1" y2="0">
        <stop offset="0" stop-color="#3a3b3d"/><stop offset=".7" stop-color="#58595b"/><stop offset="1" stop-color="#6d6e71"/>
      </linearGradient>
    </defs>
    <polygon points="0,0 300,0 282,25 300,50 0,50" fill="url(#greyRibbon)"/>
    <polyline points="0,4 290,4 274,25 290,46 0,46" fill="none" stroke="#ffffff" stroke-opacity=".45" stroke-dasharray="3 2"/>
  </svg>
  <div class="abs back-ribbon-text">Are you looking for reliable<br>Relines And Repairs</div>

  <p class="abs story">for the last 40 years, we've prided ourselves on<br>top quality customer service. Whether you need<br>new dentures, partials, relines or repairs, we have<br>the experience and skill to get the job done right.</p>

  <svg class="abs back-hex" viewBox="0 0 90 80" role="img" aria-label="Technician repairing a denture">
    <defs>
      <linearGradient id="hexBack" x1="0" y1="0" x2="1" y2="1">
        <stop offset="0" stop-color="#9a9ca0"/><stop offset=".5" stop-color="#e3c9c4"/><stop offset="1" stop-color="#eeeeee"/>
      </linearGradient>
    </defs>
    <polygon points="22,2 68,2 88,40 68,78 22,78 2,40" fill="url(#hexBack)" stroke="#bcbec0" stroke-width="3"/>
  </svg>

  <p class="abs same-day">Relines and repairs can be done the SAME day.</p>
  <div class="abs call-today">Call Velmora Dental Lab today.</div>
  <div class="abs back-phone">708-555-0194</div>
  <div class="abs back-address">48207 N Cobbet ave Brenhaven NV</div>

  <div class="abs stamp-slot" aria-hidden="true"></div>
  <div class="abs address-slot" aria-hidden="true"></div>
</section>

</body>
</html>
```